Skiing Event needs a promotional flyer designed

4 Page A4 brochure to be designed to promote a schools ski event hosted in New Zealand. The brochure will entice School teachers and school students to enter the event. The brochure will provide a basic overview of the event - dates, venue, race options and promote some of the key features of the host mountain.
Event logo has been included. Design overview with copy has been included as word document. Images have been attached that can be used or alternatives sourced. A PDF document has been included of a design example that we like.

Target Market(s)

School Teachers and School Students

Industry/Entity Type

Tourism

Requirements
Must have
• 4 page, A4 portrait document. Must include logo

```html
<!DOCTYPE html>
<html lang="en">
<head>
<meta charset="utf-8">
<title>Mt Alder Ski Challenge 2018 – Brochure Spread</title>
<link href="https://fonts.googleapis.com/css2?family=Open+Sans:wght@300;400;600;700&display=swap" rel="stylesheet">
<style>
:root{
  --blue:#29a8e0;
  --blue-dark:#1a8fc9;
  --ink:#2b2b2b;
  --mist:#dbeaf6;
  --frame:#5a5a5a;
  --white:#ffffff;
}
*{margin:0;padding:0;box-sizing:border-box}
html,body{width:1200px;height:848px;overflow:hidden;background:var(--white)}
body{font-family:"Open Sans",Arial,sans-serif;color:var(--ink);font-weight:300}
.spread{position:relative;width:1200px;height:848px;overflow:hidden}
.page{position:absolute;top:0;height:848px;width:600px;overflow:hidden}
.page--left{left:0;background:var(--white)}
.page--right{left:600px;background:linear-gradient(90deg,#e6f0f9 0%,#ffffff 22%,#ffffff 100%)}
.bands{position:absolute;inset:0;width:1200px;height:848px}
.block{position:absolute;font-size:13.4px;line-height:17.2px}
.heading{display:flex;align-items:flex-start;gap:6px;color:var(--blue);font-weight:700;font-size:14.2px;line-height:17px;text-transform:uppercase;margin-bottom:10px}
.heading svg{flex:none;width:13px;height:13px;margin-top:2px}
.align-right{text-align:right}
.align-right .heading{justify-content:flex-end}
.photo{position:absolute;border:3px solid var(--frame);box-shadow:3px 4px 4px rgba(0,0,0,.35)}
.photo--boots{left:300px;top:54px;width:300px;height:272px;background:linear-gradient(135deg,#d9dde0,#8a8f95 40%,#3a3d42 70%,#c9ced2)}
.photo--lift{left:-3px;top:374px;width:303px;height:348px;background:linear-gradient(180deg,#b7c4cf 0%,#6f7f70 28%,#f1f3f5 45%,#c4c9ce 100%)}
.photo--skis{left:906px;top:65px;width:264px;height:180px;background:linear-gradient(160deg,#1c2230 0%,#8fb5dc 35%,#e8eef5 65%,#c53b4a 100%)}
.photo--rider{left:628px;top:582px;width:264px;height:180px;background:linear-gradient(180deg,#5d7896 0%,#a9b9c8 35%,#2d3037 60%,#e9eef2 100%)}
.photo--snow{left:908px;top:582px;width:264px;height:180px;background:linear-gradient(150deg,#dfe6ec 0%,#aeb6bd 45%,#6f8a3c 60%,#2f3d52 100%)}
.facts{list-style:none;font-size:13.4px;line-height:17.2px}
.facts li{display:flex;align-items:center;gap:8px}
.facts svg{width:11px;height:11px;flex:none}
.venue{font-weight:600;font-size:13.4px;margin:22px 0 14px}
.footer{position:absolute;left:600px;top:790px;width:600px;height:58px;background:var(--blue);display:flex;align-items:center;justify-content:center;color:var(--white);font-weight:700;font-size:17.6px}
</style>
</head>
<body>
<svg width="0" height="0" style="position:absolute">
  <defs>
    <symbol id="chev-blue" viewBox="0 0 14 14"><circle cx="7" cy="7" r="7" fill="#29a8e0"/><path d="M5.5 3.8 8.7 7 5.5 10.2" fill="none" stroke="#fff" stroke-width="2"/></symbol>
    <symbol id="chev-dark" viewBox="0 0 14 14"><circle cx="7" cy="7" r="7" fill="#2b2b2b"/><path d="M5.5 3.8 8.7 7 5.5 10.2" fill="none" stroke="#fff" stroke-width="2"/></symbol>
    <linearGradient id="mist" x1="0" x2="1" y1="0" y2="0"><stop offset="0" stop-color="#dbeaf6"/><stop offset="1" stop-color="#ffffff"/></linearGradient>
  </defs>
</svg>

<div class="spread">
  <section class="page page--left"></section>
  <section class="page page--right"></section>

  <svg class="bands" viewBox="0 0 1200 848" aria-hidden="true">
    <rect x="300" y="374" width="300" height="348" fill="url(#mist)"/>
    <rect x="0" y="770" width="600" height="78" fill="url(#mist)" transform="rotate(180 300 809)"/>
    <polygon points="46,18 600,18 600,54 300,54 280,30 46,30" fill="#29a8e0"/>
    <polygon points="0,338 580,338 574,350 316,350 296,374 0,374" fill="#29a8e0"/>
    <polygon points="29,732 600,732 600,770 304,770 284,746 29,746" fill="#29a8e0"/>
    <polygon points="630,18 1200,18 1200,54 904,54 884,30 630,30" fill="#29a8e0"/>
  </svg>

  <div class="photo photo--boots" role="img" aria-label="Circle of ski boots in the snow seen from above"></div>
  <div class="photo photo--lift" role="img" aria-label="Chairlift running up a snowy slope with pine trees"></div>
  <div class="photo photo--skis" role="img" aria-label="Row of skis lined up on the snow"></div>
  <div class="photo photo--rider" role="img" aria-label="Skier in a helmet resting on a slope above the mountains"></div>
  <div class="photo photo--snow" role="img" aria-label="Ski tips buried in fresh powder snow"></div>

  <article class="block" style="left:30px;top:42px;width:262px">
    <h2 class="heading"><svg><use href="#chev-blue"/></svg>Introduction</h2>
    <p>We are extremely excited to announce the 2018 Mt Alder Ski Challenge. The event will bring together students from Australia and New Zealand locals to face off on the slopes of Mt Alder. The event is suitable for novices through to serious skiers and snowboarders.No race experience is necessary in order to compete, just a willingness to have a go. The event package offers five fantastic days in the largest skiable area in the South Island of New Zealand. It addition to the two race days participants will receive two days of training as well as a free ski day following the event.</p>
  </article>

  <article class="block align-right" style="left:316px;top:367px;width:268px">
    <h2 class="heading"><svg><use href="#chev-blue"/></svg>Where</h2>
    <p>Held on Mt Alder in the Canterbury region of the South Island of New Zealand. The Mountain reaches 2086 metres at its highest point and receives an average of 4 metres of snow a year</p>
    <h2 class="heading" style="margin-top:14px"><svg><use href="#chev-blue"/></svg>When</h2>
    <p style="font-weight:400">WEDNESDAY 11th JULY<br>THURSDAY 12th JULY 2018</p>
    <h2 class="heading" style="margin-top:14px"><svg><use href="#chev-blue"/></svg>Who</h2>
    <p>The event is open to high school age students from across Australia. The event is open to novice and holiday skiers to experienced skiers and snowboarders. Prizes will be given in different year categories for both Male and Female skiers as well as overall school prizes.</p>
  </article>

  <article class="block" style="left:30px;top:752px;width:520px">
    <h2 class="heading"><svg><use href="#chev-blue"/></svg>The Competition</h2>
    <p style="color:#555">Two race formats will be offered – Slalom and Duel Slalom for both Skiers and Snowboarders</p>
  </article>

  <article class="block" style="left:629px;top:42px;width:270px">
    <h2 class="heading"><svg><use href="#chev-blue"/></svg>Include infographics for<br>the below</h2>
    <ul class="facts">
      <li><svg><use href="#chev-dark"/></svg>365 hectares of skiable area</li>
      <li><svg><use href="#chev-dark"/></svg>4 Freestyle terrain parks</li>
      <li><svg><use href="#chev-dark"/></svg>Longest Run – 2kms</li>
      <li><svg><use href="#chev-dark"/></svg>Highest Point – 2086 Metres</li>
      <li><svg><use href="#chev-dark"/></svg>Average Snowfall – 4 Metres</li>
      <li><svg><use href="#chev-dark"/></svg>75 Snow Guns</li>
    </ul>
  </article>

  <article class="block" style="left:629px;top:232px;width:540px">
    <h2 class="heading"><svg><use href="#chev-blue"/></svg>Accommodation</h2>
    <p>Your accommodation base for the event will be the town of Methven, nestled in the foothills of the Southern Alps and Mt Alder. With a number of cafes, restaurants, takeaway options and two supermarkets the town provides a great base for making the most of New Zealand’s best ski field.</p>
    <h3 class="venue">ALPINE CREST LODGE</h3>
    <p>With a variety of different rooming options and facilities including large lounge with pool table and cosy fire, separate dining room, meeting room and swimming pool, it is the ideal base for schools.</p>
    <h3 class="venue">KOWHAI RIDGE</h3>
    <p>Kowhai Ridge Resort is a High Countryself contained accommodation style resort in the heartland village of Methven. Accommodation options include studios and two bedroom apartments, facilities include an onsite restaurant, outdoor spa pools, tennis courts, chip &amp; putting green and laundry facilities.</p>
  </article>

  <footer class="footer">www.alderskichallenge.com.au</footer>
</div>
</body>
</html>
```